Design a Ketone Test Strip Label and Box for Formed From Vale

Design a product label and a box design for a Ketone Test Strip product for the company Formed From Vale.
*Please use the template of the box and label .ai file will be provided.*
Please see example of other competitors for inspiration
Use the text/look instructions from the provided product examples
*MUST HAVE BARCODE ON BOX*

Industry/Entity Type

It Company

Font styles to use
Sans Serif

Colors

Designer to choose colors to be used in the design.

Requirements
Must have
• *MUST HAVE BARCODE ON BOX*
• Must use the .ai templates provided.
• LEFT OF LABEL Layout/text:
• FormedFromVale.com
• Formed From Vale Logo
• MFG:
• EXP:
• IMPORTANT
• Keep away from light and moisture.
• Promptly replace cap after taking out strips.
• Do not remove desiccants.
• Do not touch test areas of reagent strips.
• Use within the expiration date.
• Read insert carefully before use.
• 100 Ketone Test Strips
• MIDDLE/RIGHT SIDE OF LABEL layout/text:
• KETONE TEST STRIPS
• (to the left) TESTING COLOR CHART (going down vertically)
• (to the right) Love Keto? Visit: FormedFromVale.com
• How to test
• 1.Firmly hold end farthest away from test pad. Pass test pad through
• urine stream or place inside a urine filled cup
• 2. After 40 seconds, match the test pad
• to the color chart shown on the bottle.
• Any other symbols in the template placed at the bottom.
• FRONT OF BOX:
• Formed From Vale Logo
• Ketone Test Strips
• Reagent Strips for Urinalysis
• Color Chart Going Horizontal
• Instant Results
• Most Accurate
• Easy to Use
• Pharmaceutical Grade
• 100 Strips
• LEFT OF BOX:
• RIGHT OF BOX:
• BACK OF BOX:
Nice to have
• Clean simple design
Should not have
• be too busy

```html
<!DOCTYPE html>
<html lang="en">
<head>
<meta charset="utf-8">
<title>Formed From Vale – Keton Test Strips Packaging</title>
<link rel="stylesheet" href="https://fonts.googleapis.com/css2?family=Montserrat:wght@400;500;600;700&family=Arimo:wght@400;700&family=Barlow+Semi+Condensed:wght@600&display=swap">
<style>
  :root {
    --brand-blue: #2f76b6;
    --band-blue: #2e76bd;
    --ink: #333333;
    --pill: #4a4a4a;
    --paper: #f3f3f3;
    --page: #ffffff;
    --frame: #c8c8c8;
    --swatch-1: #7fa6d6;
    --swatch-2: #5888c6;
    --swatch-3: #3c67a1;
    --swatch-4: #2c4a7b;
    --swatch-5: #1b2d4b;
  }
  * { box-sizing: border-box; margin: 0; padding: 0; }
  html, body { width: 1037px; height: 1200px; overflow: hidden; background: var(--page); }
  .canvas {
    position: relative; width: 1037px; height: 1200px;
    border: 1px solid var(--frame); background: var(--page);
  }
  .panel { position: absolute; background: var(--paper); overflow: hidden; }
  .chevron { position: absolute; left: 0; top: 0; width: 100%; }

  .brand-name {
    position: absolute; left: 0; width: 100%; text-align: center;
    font-family: "Montserrat", sans-serif; font-weight: 600; color: #ffffff;
    letter-spacing: .12em; text-transform: uppercase; line-height: 1.15; white-space: nowrap;
  }
  .product-name {
    position: absolute; left: 0; width: 100%; text-align: center;
    font-family: "Montserrat", sans-serif; font-weight: 600; color: var(--brand-blue);
    letter-spacing: .16em; line-height: 1; text-indent: .16em;
  }
  .product-pill {
    position: absolute; background: var(--pill); color: #ffffff; border-radius: 3px;
    font-family: "Montserrat", sans-serif; font-weight: 700; text-align: center;
    letter-spacing: .16em; white-space: nowrap;
  }
  .tagline {
    position: absolute; left: 0; width: 100%; text-align: center;
    font-family: "Arimo", sans-serif; color: var(--ink); white-space: nowrap;
  }
  .color-chart { position: absolute; display: flex; }
  .color-chart span { display: block; }
  .benefits { position: absolute; list-style: none; font-family: "Arimo", sans-serif; font-weight: 700; color: var(--ink); }
  .benefits li { display: flex; align-items: center; white-space: nowrap; }
  .benefits svg { flex: none; }
  .count-band {
    position: absolute; left: 0; width: 100%; background: var(--band-blue); color: #ffffff;
    text-align: center; font-family: "Barlow Semi Condensed", sans-serif; font-weight: 600;
    letter-spacing: .03em;
  }

  /* Box front */
  .box-front { left: 190px; top: 175px; width: 360px; height: 870px; }
  .box-front .brand-name { top: 192px; font-size: 24px; }
  .box-front .product-name { top: 474px; font-size: 40px; }
  .box-front .product-pill { left: 95px; top: 514px; width: 175px; height: 23px; font-size: 17px; line-height: 23px; }
  .box-front .tagline { top: 577px; font-size: 14.5px; }
  .box-front .color-chart { left: 57px; top: 603px; gap: 16px; }
  .box-front .color-chart span { width: 36px; height: 30px; }
  .box-front .benefits { left: 80px; top: 676px; font-size: 16.5px; }
  .box-front .benefits li { height: 25px; gap: 4px; }
  .box-front .count-band { top: 843px; height: 27px; font-size: 16px; line-height: 27px; }

  /* Bottle label */
  .bottle-label { left: 590px; top: 575px; width: 223px; height: 475px; }
  .bottle-label .chevron { left: 15px; width: 190px; }
  .bottle-label .brand-name { top: 106px; font-size: 13px; }
  .bottle-label .product-name { top: 257px; font-size: 21px; }
  .bottle-label .product-pill { left: 64px; top: 279px; width: 94px; height: 12px; font-size: 8.5px; line-height: 12px; }
  .bottle-label .tagline { top: 313px; font-size: 8px; }
  .bottle-label .color-chart { left: 43px; top: 327px; gap: 7.6px; }
  .bottle-label .color-chart span { width: 20px; height: 16px; }
  .bottle-label .benefits { left: 56px; top: 364px; font-size: 8.5px; }
  .bottle-label .benefits li { height: 13.5px; gap: 2px; }
  .bottle-label .count-band { top: 442px; height: 17px; font-size: 10.5px; line-height: 17px; }

  .s1 { background: var(--swatch-1); } .s2 { background: var(--swatch-2); }
  .s3 { background: var(--swatch-3); } .s4 { background: var(--swatch-4); }
  .s5 { background: var(--swatch-5); }
</style>
</head>
<body>
<main class="canvas">

  <section class="panel box-front" aria-label="Box front">
    <svg class="chevron" viewBox="0 0 360 437" height="437" aria-hidden="true">
      <polygon points="0,0 360,0 360,342 180,437 0,342" fill="var(--brand-blue)"/>
    </svg>
    <div class="brand-name">Formed From Vale</div>
    <h1 class="product-name">KETON</h1>
    <div class="product-pill">TEST STRIPS</div>
    <p class="tagline">REAGENT STRIPS FOR URINALYSIS</p>
    <div class="color-chart" aria-label="Colour chart">
      <span class="s1"></span><span class="s2"></span><span class="s3"></span><span class="s4"></span><span class="s5"></span>
    </div>
    <ul class="benefits">
      <li><svg width="16" height="16" viewBox="0 0 16 16"><rect x="1" y="1" width="14" height="14" fill="none" stroke="var(--ink)" stroke-width="1.2"/><path d="M4 8l3 3 6-8" fill="none" stroke="var(--ink)" stroke-width="1.4"/></svg>RESULTS IN SECONDS</li>
      <li><svg width="16" height="16" viewBox="0 0 16 16"><rect x="1" y="1" width="14" height="14" fill="none" stroke="var(--ink)" stroke-width="1.2"/><path d="M4 8l3 3 6-8" fill="none" stroke="var(--ink)" stroke-width="1.4"/></svg>HIGH QUALITY</li>
      <li><svg width="16" height="16" viewBox="0 0 16 16"><rect x="1" y="1" width="14" height="14" fill="none" stroke="var(--ink)" stroke-width="1.2"/><path d="M4 8l3 3 6-8" fill="none" stroke="var(--ink)" stroke-width="1.4"/></svg>EASY TO USE</li>
      <li><svg width="16" height="16" viewBox="0 0 16 16"><rect x="1" y="1" width="14" height="14" fill="none" stroke="var(--ink)" stroke-width="1.2"/><path d="M4 8l3 3 6-8" fill="none" stroke="var(--ink)" stroke-width="1.4"/></svg>PROFESSIONAL GRADE</li>
    </ul>
    <div class="count-band">100 STRIPS</div>
  </section>

  <section class="panel bottle-label" aria-label="Bottle label">
    <svg class="chevron" viewBox="0 0 190 237" height="237" aria-hidden="true">
      <polygon points="0,0 190,0 190,187 95,237 0,187" fill="var(--brand-blue)"/>
    </svg>
    <div class="brand-name">Formed From Vale</div>
    <h2 class="product-name">KETON</h2>
    <div class="product-pill">TEST STRIPS</div>
    <p class="tagline">REAGENT STRIPS FOR URINALYSIS</p>
    <div class="color-chart" aria-label="Colour chart">
      <span class="s1"></span><span class="s2"></span><span class="s3"></span><span class="s4"></span><span class="s5"></span>
    </div>
    <ul class="benefits">
      <li><svg width="9" height="9" viewBox="0 0 16 16"><rect x="1" y="1" width="14" height="14" fill="none" stroke="var(--ink)" stroke-width="1.6"/><path d="M4 8l3 3 6-8" fill="none" stroke="var(--ink)" stroke-width="2"/></svg>RESULTS IN SECONDS</li>
      <li><svg width="9" height="9" viewBox="0 0 16 16"><rect x="1" y="1" width="14" height="14" fill="none" stroke="var(--ink)" stroke-width="1.6"/><path d="M4 8l3 3 6-8" fill="none" stroke="var(--ink)" stroke-width="2"/></svg>HIGH QUALITY</li>
      <li><svg width="9" height="9" viewBox="0 0 16 16"><rect x="1" y="1" width="14" height="14" fill="none" stroke="var(--ink)" stroke-width="1.6"/><path d="M4 8l3 3 6-8" fill="none" stroke="var(--ink)" stroke-width="2"/></svg>EASY TO USE</li>
      <li><svg width="9" height="9" viewBox="0 0 16 16"><rect x="1" y="1" width="14" height="14" fill="none" stroke="var(--ink)" stroke-width="1.6"/><path d="M4 8l3 3 6-8" fill="none" stroke="var(--ink)" stroke-width="2"/></svg>PROFESSIONAL GRADE</li>
    </ul>
    <div class="count-band">100 STRIPS</div>
  </section>

</main>
</body>
</html>
```